Boutique Fitness Center needs a front window / door wrap

We need a front door and window wrap for our new fitness location called VaroLume. We are a higher end, boutique body transformation center that will be opening soon.

We are looking to have 2 medium windows and 2 glass doors that are in the front of the facility wrapped - drawing attention to our facility in a bold, but classy way.

Our colors are Black, Yellow, Gray and White

There should be some artistic elements to the design.

I have attached a photo of our building. We are having a large 15' x 5' sign hung above the awning with our logo (logo also attached for reference)

The measurements for the 2 doors and 2 windows are as follows:
Both Doors: 30. 75" wide x 70.5" High
Both Windows: 73" wide x 59" High

Our ideas for the two doors are that on door one (door to left of picture) have the word "CONFIDENCE" in yellow written vertically with a light ghost image in the background of someone working out, possibly doing push-ups or battle ropes.

And on door #2 (door to the right of the picture) have the word "ESTEEM" written vertically in yellow with some type of light ghost image in the background

I have attached an example photo of where I got the idea of having large bold letters vertically written on the doors.

On the two large windows to the far left and right, I'd like to have a workout image of a female on one window and a male on the other doing a movement such slam balls, battle ropes, push-ups, etc. (No big bodybuilders, no image of traditional workout machines)

The window images should be done in black, white and gray colors.

I have attached an example image of a gym in New York, 81K, that I really like how the image is black and white with a pop of yellow.

On the Far Right window I would also like to have the text "Change Begins Here" with maybe an curved arrow pointing to the door.
The text should be distressed looking, similar to our logo and this is where pops of yellow can be added.

Use the example photos I've attached as reference and I'm excited to see what you're able to come up with.

```html
<!DOCTYPE html>
<html lang="en">
<head>
<meta charset="utf-8">
<title>VaroLume Storefront Wrap</title>
<link rel="stylesheet" href="https://fonts.googleapis.com/css2?family=Archivo+Black&family=Rubik+Dirt&family=Montserrat:wght@600&display=swap">
<style>
  :root {
    --backdrop: #d9d9d6;
    --frame: #1f2328;
    --ink: #050505;
    --yellow: #ffe600;
    --white: #f2f2f2;
    --gray-light: #9a9a9a;
    --gray-mid: #4a4a4a;
    --gray-dark: #1a1a1a;
  }
  * { box-sizing: border-box; margin: 0; padding: 0; }
  html, body { width: 1200px; height: 900px; overflow: hidden; }
  body {
    background: var(--backdrop);
    display: flex;
    align-items: center;
    justify-content: center;
  }
  .wrap-set {
    display: flex;
    align-items: flex-start;
    gap: 16px;
  }
  .wrap-set .door + .door { margin-left: 54px; }

  .panel {
    position: relative;
    background: var(--ink);
    border: 6px solid var(--frame);
    overflow: hidden;
  }
  .window { width: 365px; height: 295px; }
  .door { width: 154px; height: 353px; }

  .photo { position: absolute; }

  /* Left window */
  .window-brand .photo {
    left: 78px; top: 0; right: 0; bottom: 0;
    background: radial-gradient(ellipse at 45% 40%, var(--gray-light) 0%, var(--gray-mid) 40%, var(--gray-dark) 75%, var(--ink) 100%);
  }
  .brand-name {
    position: absolute;
    left: 6px; bottom: 8px;
    writing-mode: vertical-rl;
    transform: rotate(180deg);
    white-space: nowrap;
    font-family: "Archivo Black", sans-serif;
    font-size: 44px;
    line-height: 1;
    color: var(--yellow);
  }
  .brand-tagline {
    position: absolute;
    left: 54px; bottom: 30px;
    writing-mode: vertical-rl;
    transform: rotate(180deg);
    white-space: nowrap;
    font-family: "Montserrat", sans-serif;
    font-weight: 600;
    font-size: 8px;
    letter-spacing: 1.6px;
    color: var(--yellow);
  }

  /* Doors */
  .door-confidence .photo {
    left: 6px; top: 40px; width: 90px; height: 230px;
    background: radial-gradient(ellipse at 50% 45%, var(--gray-light) 0%, var(--gray-mid) 45%, var(--ink) 80%);
    opacity: 0.8;
  }
  .door-esteem .photo {
    left: 0; top: 90px; width: 90px; height: 160px;
    background: radial-gradient(ellipse at 45% 45%, var(--gray-light) 0%, var(--gray-mid) 40%, var(--ink) 80%);
    opacity: 0.75;
  }
  .door-word {
    position: absolute;
    bottom: 12px;
    writing-mode: vertical-rl;
    transform: rotate(180deg);
    white-space: nowrap;
    color: var(--yellow);
    line-height: 1;
  }
  .word-confidence {
    right: 12px;
    font-family: "Archivo Black", sans-serif;
    font-size: 36px;
  }
  .word-esteem {
    right: 16px;
    font-family: "Rubik Dirt", sans-serif;
    font-size: 46px;
  }

  /* Right window */
  .window-message .arrow {
    position: absolute;
    left: 12px; top: 60px;
    width: 56px; height: 150px;
  }
  .message {
    position: absolute;
    left: 82px; top: 84px;
    font-family: "Rubik Dirt", sans-serif;
    line-height: 1;
    color: var(--yellow);
    white-space: nowrap;
  }
  .message span { display: block; }
  .msg-change { font-size: 42px; }
  .msg-begins { font-size: 32px; color: var(--white); margin-left: 80px; }
  .msg-here { font-size: 50px; margin-left: 32px; }
</style>
</head>
<body>
  <main class="wrap-set">
    <section class="panel window window-brand">
      <div class="photo" role="img" aria-label="Black and white photo of a fit man and woman training with a slam ball"></div>
      <div class="brand-name">VaroLume</div>
      <div class="brand-tagline">PERSONAL GROUP TRAINING</div>
    </section>

    <section class="panel door door-confidence">
      <div class="photo" role="img" aria-label="Faint ghost image of a woman holding a kettlebell"></div>
      <div class="door-word word-confidence">CONFIDENCE</div>
    </section>

    <section class="panel door door-esteem">
      <div class="photo" role="img" aria-label="Faint ghost image of a man in a training stance"></div>
      <div class="door-word word-esteem">ESTEEM</div>
    </section>

    <section class="panel window window-message">
      <svg class="arrow" viewBox="0 0 56 150" aria-hidden="true">
        <polygon points="0,60 36,0 36,150" fill="var(--yellow)"/>
        <rect x="36" y="20" width="18" height="130" fill="var(--yellow)"/>
      </svg>
      <div class="message">
        <span class="msg-change">CHANGE</span>
        <span class="msg-begins">BEGINS</span>
        <span class="msg-here">HERE</span>
      </div>
    </section>
  </main>
</body>
</html>
```